I am wanting to develop a new range of products called “SWIFT LINE”. It will be 500mL trigger bottles of ready to use cleaning products. A Window&Glass Cleaner, Surface Sanitiser, Room Deodourant, Stainless Steel Rub, Spray&Wipe and a Sanitising Spray & Wipe. The label dimensions and shape are attached. Marlow is the shape I want but I do not like the design so don't base your design on it. FRESHDASH is a design I like I also like the design on the coffee packaging.

Retail and commercial kitchen

Cleaning Product

```html
<!DOCTYPE html>
<html lang="en">
<head>
<meta charset="utf-8">
<title>SWIFT LINE – Label Range</title>
<link rel="stylesheet" href="https://fonts.googleapis.com/css2?family=Jost:wght@400;500;700&display=swap">
<style>
  :root {
    --canvas: #f1f2f3;
    --label-paper: #ffffff;
    --label-edge: #c9cbcd;
    --ink-light: #ffffff;
    --tone-green: #4cc75a;
    --tone-green-soft: #b7e6b3;
    --tone-red: #dd2f3b;
    --tone-red-soft: #f4b3b7;
    --tone-teal: #2dc4cf;
    --tone-teal-soft: #aee6ea;
  }
  * { margin: 0; padding: 0; box-sizing: border-box; }
  html, body {
    width: 1200px;
    height: 675px;
    overflow: hidden;
    background: var(--canvas);
  }
  .range {
    width: 1200px;
    height: 675px;
    display: flex;
    align-items: center;
    justify-content: center;
    gap: 60px;
  }
  .label { width: 300px; height: 440px; }
  .label--green { --tone: var(--tone-green); --tone-soft: var(--tone-green-soft); }
  .label--red   { --tone: var(--tone-red);   --tone-soft: var(--tone-red-soft); }
  .label--teal  { --tone: var(--tone-teal);  --tone-soft: var(--tone-teal-soft); }

  .label__paper { fill: var(--label-paper); stroke: var(--label-edge); stroke-width: 1.2; }
  .stop-tone { stop-color: var(--tone); }
  .stop-soft { stop-color: var(--tone-soft); }

  .label__name {
    font-family: 'Jost', sans-serif;
    font-weight: 700;
    font-size: 40px;
    fill: var(--ink-light);
    letter-spacing: 0.5px;
  }
  .label__rule { stroke: var(--ink-light); stroke-width: 2; }
  .label__claim {
    font-family: 'Jost', sans-serif;
    font-weight: 500;
    font-size: 19px;
    fill: var(--ink-light);
  }
  .label__product {
    font-family: 'Jost', sans-serif;
    font-weight: 500;
    font-size: 9.5px;
    fill: var(--ink-light);
    letter-spacing: 0.2px;
  }
  .label__volume {
    font-family: 'Jost', sans-serif;
    font-weight: 400;
    font-size: 9px;
    fill: var(--ink-light);
  }
</style>
</head>
<body>
<main class="range">

  <svg class="label label--green" viewBox="0 0 300 440" aria-label="SWIFT LINE Surface Sanitiser label">
    <defs>
      <clipPath id="shape-green">
        <path d="M22 92 L258 22 Q290 13 290 46 L290 402 Q290 430 262 430 L38 430 Q10 430 10 402 L10 112 Q10 96 22 92 Z"/>
      </clipPath>
      <radialGradient id="art-green" cx="50%" cy="50%" r="50%">
        <stop class="stop-tone" offset="0.6"/>
        <stop class="stop-soft" offset="1"/>
      </radialGradient>
      <linearGradient id="base-green" x1="0" y1="0" x2="0" y2="1">
        <stop class="stop-soft" offset="0"/>
        <stop class="stop-tone" offset="0.55"/>
      </linearGradient>
    </defs>
    <path class="label__paper" d="M22 92 L258 22 Q290 13 290 46 L290 402 Q290 430 262 430 L38 430 Q10 430 10 402 L10 112 Q10 96 22 92 Z"/>
    <g clip-path="url(#shape-green)">
      <circle cx="158" cy="235" r="98" fill="url(#art-green)" role="img" aria-label="Overlapping translucent colour blobs with bubbles behind the product name"/>
      <rect x="0" y="360" width="300" height="80" fill="url(#base-green)" role="img" aria-label="Bubbly colour wave along the label base"/>
    </g>
    <text class="label__name" x="158" y="215" text-anchor="middle">SWIFT</text>
    <text class="label__name" x="158" y="254" text-anchor="middle">LINE</text>
    <line class="label__rule" x1="112" y1="262" x2="204" y2="262"/>
    <text class="label__claim" x="158" y="282" text-anchor="middle">READY TO USE</text>
    <text class="label__product" x="158" y="296" text-anchor="middle">SURFACE SANITISER</text>
    <text class="label__volume" x="275" y="418" text-anchor="end">500 ml / 16.9oz</text>
  </svg>

  <svg class="label label--red" viewBox="0 0 300 440" aria-label="SWIFT LINE Sanitising Spray and Wipe label">
    <defs>
      <clipPath id="shape-red">
        <path d="M22 92 L258 22 Q290 13 290 46 L290 402 Q290 430 262 430 L38 430 Q10 430 10 402 L10 112 Q10 96 22 92 Z"/>
      </clipPath>
      <radialGradient id="art-red" cx="50%" cy="50%" r="50%">
        <stop class="stop-tone" offset="0.6"/>
        <stop class="stop-soft" offset="1"/>
      </radialGradient>
      <linearGradient id="base-red" x1="0" y1="0" x2="0" y2="1">
        <stop class="stop-soft" offset="0"/>
        <stop class="stop-tone" offset="0.55"/>
      </linearGradient>
    </defs>
    <path class="label__paper" d="M22 92 L258 22 Q290 13 290 46 L290 402 Q290 430 262 430 L38 430 Q10 430 10 402 L10 112 Q10 96 22 92 Z"/>
    <g clip-path="url(#shape-red)">
      <circle cx="158" cy="235" r="98" fill="url(#art-red)" role="img" aria-label="Overlapping translucent colour blobs with bubbles behind the product name"/>
      <rect x="0" y="360" width="300" height="80" fill="url(#base-red)" role="img" aria-label="Bubbly colour wave along the label base"/>
    </g>
    <text class="label__name" x="158" y="215" text-anchor="middle">SWIFT</text>
    <text class="label__name" x="158" y="254" text-anchor="middle">LINE</text>
    <line class="label__rule" x1="112" y1="262" x2="204" y2="262"/>
    <text class="label__claim" x="158" y="282" text-anchor="middle">READY TO USE</text>
    <text class="label__product" x="158" y="296" text-anchor="middle">SANITISING SPRAY &amp; WIPE</text>
    <text class="label__volume" x="275" y="418" text-anchor="end">500 ml / 16.9oz</text>
  </svg>

  <svg class="label label--teal" viewBox="0 0 300 440" aria-label="SWIFT LINE Window and Glass Cleaner label">
    <defs>
      <clipPath id="shape-teal">
        <path d="M22 92 L258 22 Q290 13 290 46 L290 402 Q290 430 262 430 L38 430 Q10 430 10 402 L10 112 Q10 96 22 92 Z"/>
      </clipPath>
      <radialGradient id="art-teal" cx="50%" cy="50%" r="50%">
        <stop class="stop-tone" offset="0.6"/>
        <stop class="stop-soft" offset="1"/>
      </radialGradient>
      <linearGradient id="base-teal" x1="0" y1="0" x2="0" y2="1">
        <stop class="stop-soft" offset="0"/>
        <stop class="stop-tone" offset="0.55"/>
      </linearGradient>
    </defs>
    <path class="label__paper" d="M22 92 L258 22 Q290 13 290 46 L290 402 Q290 430 262 430 L38 430 Q10 430 10 402 L10 112 Q10 96 22 92 Z"/>
    <g clip-path="url(#shape-teal)">
      <circle cx="158" cy="235" r="98" fill="url(#art-teal)" role="img" aria-label="Overlapping translucent colour blobs with bubbles behind the product name"/>
      <rect x="0" y="360" width="300" height="80" fill="url(#base-teal)" role="img" aria-label="Bubbly colour wave along the label base"/>
    </g>
    <text class="label__name" x="158" y="215" text-anchor="middle">SWIFT</text>
    <text class="label__name" x="158" y="254" text-anchor="middle">LINE</text>
    <line class="label__rule" x1="112" y1="262" x2="204" y2="262"/>
    <text class="label__claim" x="158" y="282" text-anchor="middle">READY TO USE</text>
    <text class="label__product" x="158" y="296" text-anchor="middle">WINDOW &amp; GLASS CLEANER</text>
    <text class="label__volume" x="275" y="418" text-anchor="end">500 ml / 16.9oz</text>
  </svg>

</main>
</body>
</html>
```